Velquora Design
Would like the design to go over the page in a way that can type over it.
We are a personal training and small group studio
Want it to be professional and classy
Updates
Project Deadline Extended
Reason: Asked for some modifications on a few designs, want to give the designers time to do this
Target Market(s)
All age groups, sports professionals as well as business professionals, families
Industry/Entity Type
Training
Requirements
Must have
- Must have Velquora Studio
Mina Tellaver
214 Barnicot Lane
Wexcombe Vale
South Australia 5173
Phone: 0438917263
Nice to have
- Professional classy fonts
Colour
Should not have
- Clip art
Balloons

```html
<!DOCTYPE html>
<html lang="en">
<head>
<meta charset="utf-8">
<title>Velquora Studio Letterhead</title>
<link rel="stylesheet" href="https://fonts.googleapis.com/css2?family=Open+Sans:wght@400;700&display=swap">
<style>
  :root {
    --backdrop: #3a3a3a;
    --paper: #ffffff;
    --brand-blue: #1e88d6;
    --wave-blue: #8cc3ee;
    --wave-fade: #ffffff;
    --body-text: #555555;
  }
  html, body {
    margin: 0;
    padding: 0;
    width: 1200px;
    height: 907px;
    overflow: hidden;
    background: var(--backdrop);
  }
  .canvas {
    position: relative;
    width: 1200px;
    height: 907px;
  }
  .letterhead {
    position: absolute;
    left: 325px;
    top: 54px;
    width: 566px;
    height: 799px;
    background: var(--paper);
    box-shadow: 0 6px 18px rgba(0, 0, 0, 0.5);
    overflow: hidden;
  }
  .wave-band {
    position: absolute;
    inset: 0;
    width: 566px;
    height: 799px;
  }
  .wave-start { stop-color: var(--wave-fade); stop-opacity: 0; }
  .wave-end { stop-color: var(--wave-blue); stop-opacity: 0.75; }
  .brand {
    position: absolute;
    right: 44px;
    top: 86px;
    display: flex;
    align-items: center;
    gap: 8px;
  }
  .brand-dot {
    width: 14px;
    height: 14px;
    border-radius: 50%;
    background: var(--brand-blue);
  }
  .brand-name {
    font-family: "Open Sans", sans-serif;
    font-weight: 700;
    font-size: 19px;
    line-height: 1;
    color: var(--brand-blue);
    letter-spacing: -0.3px;
  }
  .contact {
    position: absolute;
    left: 49px;
    top: 716px;
    font-family: "Open Sans", sans-serif;
    font-style: normal;
    font-weight: 400;
    font-size: 8px;
    line-height: 12px;
    color: var(--body-text);
  }
  .contact p { margin: 0; }
</style>
</head>
<body>
<div class="canvas">
  <section class="letterhead">
    <svg class="wave-band" viewBox="0 0 566 799">
      <defs>
        <linearGradient id="wave-top-fill" x1="0" y1="0" x2="1" y2="0">
          <stop offset="0" class="wave-start"/>
          <stop offset="1" class="wave-end"/>
        </linearGradient>
        <linearGradient id="wave-bottom-fill" x1="0" y1="0" x2="1" y2="0">
          <stop offset="0" class="wave-start"/>
          <stop offset="1" class="wave-end"/>
        </linearGradient>
      </defs>
      <path role="img" aria-label="Soft blue line-pattern wave sweeping across the top of the page"
            fill="url(#wave-top-fill)"
            d="M60 12 C200 36 300 148 430 164 C490 170 530 150 566 126
               L566 156 C530 178 490 192 430 186 C300 178 200 80 60 12 Z"/>
      <path role="img" aria-label="Soft blue line-pattern wave sweeping into the lower right corner"
            fill="url(#wave-bottom-fill)"
            d="M150 646 C260 656 330 696 420 738 C480 764 530 780 566 784
               L566 799 C530 798 480 784 420 758 C330 718 260 670 150 646 Z"/>
    </svg>

    <div class="brand">
      <span class="brand-dot"></span>
      <span class="brand-name">Velquora Studio</span>
    </div>

    <address class="contact">
      <p>Mina Tellaver</p>
      <p>214 Barnicot Lane, Wexcombe Vale, South Australia 5173</p>
      <p>Phone number: 043 891 72 63</p>
    </address>
  </section>
</div>
</body>
</html>
```